need a clean, modern job advertisement designed for social media (Facebook & Instagram).

The post is to advertise two positions:
• Leading Hand Boilermaker
• Dragline Fitter
We want the design to match our KRT Site Services branding: blue, white, strong, professional, mining-industry style.
What the design should include:
Bold headline: “WE’RE HIRING”
Sub-headline: “Leading Hand Boilermaker & Dragline Fitter”
Key points:
• Bowen Basin based
• Dragline & shovel maintenance
• Great pay + long-term work
• Locally owned & operated
KRT logo placed cleanly
Space for 1–2 images (boilermaking or dragline work)
Design style:
Strong and industrial
Blue/white colour scheme
Easy to read at a glance
Suitable for a square 1080×1080 design

```html
<!DOCTYPE html>
<html lang="en">
<head>
<meta charset="utf-8">
<title>KRT Site Services – We Are Hiring</title>
<link href="https://fonts.googleapis.com/css2?family=Anton&family=Archivo+Black&family=Oswald:wght@500&family=Poppins:wght@500;600;700&display=swap" rel="stylesheet">
<style>
  :root{
    --backdrop:#8f8e90;
    --paper:#f3f3f6;
    --ink:#1b1b1d;
    --dark:#1f1f21;
    --cyan:#08b4ec;
    --blue:#0a5ddb;
    --blue-deep:#0648c2;
    --white:#ffffff;
  }
  *{margin:0;padding:0;box-sizing:border-box}
  html,body{width:1182px;height:1200px;overflow:hidden;background:var(--backdrop)}
  .post{position:absolute;left:27px;top:36px;width:1128px;height:1128px;background:var(--paper);overflow:hidden;
    background-image:radial-gradient(circle at 0 0,rgba(0,0,0,.06),transparent 30%)}
  .dark-panel{position:absolute;left:0;top:600px;width:900px;height:528px;background:linear-gradient(135deg,#252527,#161617)}
  .art{position:absolute;inset:0}
  .kicker{position:absolute;left:77px;top:46px;font:400 70px/1 "Archivo Black",sans-serif;color:var(--ink);letter-spacing:1px}
  .headline{position:absolute;left:70px;top:112px;font:400 200px/1 "Anton",sans-serif;letter-spacing:-4px;
    background:linear-gradient(180deg,var(--cyan),var(--blue) 85%);-webkit-background-clip:text;background-clip:text;color:transparent}
  .roles{position:absolute;left:77px;top:316px;font:700 60px/65px "Poppins",sans-serif;color:var(--ink)}
  .location{position:absolute;left:0;top:564px;width:542px;height:64px;border-radius:0 32px 32px 0;
    background:linear-gradient(90deg,var(--cyan),var(--blue));border:4px solid var(--white);border-left:0;
    display:flex;align-items:center;padding-left:72px;gap:14px;color:var(--white);font:700 38px/1 "Poppins",sans-serif}
  .perks{position:absolute;left:75px;top:650px;list-style:none}
  .perks li{display:flex;align-items:center;gap:14px;height:61px;font:500 30px/1 "Poppins",sans-serif;color:var(--white)}
  .brand{position:absolute;left:75px;top:952px;width:300px;display:flex;align-items:center;gap:12px;font:700 34px/40px "Poppins",sans-serif;color:var(--white)}
  .brand-mark{flex:none;width:22px;height:22px;border-radius:50%;background:var(--cyan)}
  .contact{position:absolute;left:404px;top:984px;list-style:none}
  .contact li{display:flex;align-items:center;gap:10px;height:50px;font:500 38px/1 "Oswald",sans-serif;color:var(--white)}
  .contact svg{flex:none}
</style>
</head>
<body>
<main class="post">
  <div class="dark-panel"></div>

  <svg class="art" width="1128" height="1128" viewBox="0 0 1128 1128">
    <defs>
      <linearGradient id="siteTones" x1="0" y1="0" x2="1" y2="1">
        <stop offset="0" stop-color="#c9ccd0"/><stop offset=".5" stop-color="#8d8a84"/><stop offset="1" stop-color="#5d5a55"/>
      </linearGradient>
      <linearGradient id="weldTones" x1="0" y1="0" x2="1" y2="1">
        <stop offset="0" stop-color="#17163a"/><stop offset=".45" stop-color="#3a3f8f"/><stop offset=".6" stop-color="#b8c4ff"/><stop offset="1" stop-color="#1d1b3a"/>
      </linearGradient>
    </defs>
    <g role="img" aria-label="Megaphone graphic">
      <rect x="545" y="10" width="110" height="140" rx="14" fill="#dbe4f3"/>
    </g>
    <g role="img" aria-label="Photo of crew working on scaffolding at a mine site">
      <polygon points="789,0 1128,0 1128,402 820,402 758,522 634,292" fill="url(#siteTones)"/>
    </g>
    <g role="img" aria-label="Photo of a boilermaker welding">
      <polygon points="824,402 1128,402 1128,1128 820,1128 640,775" fill="url(#weldTones)"/>
    </g>
    <polyline points="789,0 634,292 758,522" fill="none" stroke="var(--white)" stroke-width="10"/>
    <polyline points="778,0 622,292 745,522" fill="none" stroke="var(--blue)" stroke-width="7"/>
    <polyline points="824,402 640,775 820,1128" fill="none" stroke="var(--white)" stroke-width="12"/>
    <polyline points="812,402 628,775 808,1128" fill="none" stroke="var(--blue)" stroke-width="7"/>
    <polyline points="1128,402 824,402" fill="none" stroke="var(--white)" stroke-width="6"/>
  </svg>

  <p class="kicker">WE ARE</p>
  <h1 class="headline">HIRING!</h1>
  <h2 class="roles">Leading Hand<br>Boilermaker &amp;<br>Dragline Fitter</h2>

  <div class="location">
    <svg width="26" height="34" viewBox="0 0 26 34" aria-hidden="true"><path d="M13 2a10 10 0 0 0-10 10c0 8 10 16 10 16s10-8 10-16A10 10 0 0 0 13 2z" fill="none" stroke="#fff" stroke-width="3"/><circle cx="13" cy="12" r="3.5" fill="#fff"/><path d="M4 32h18" stroke="#fff" stroke-width="3"/></svg>
    Bowen Basin based
  </div>

  <ul class="perks">
    <li><svg width="46" height="50" viewBox="0 0 46 50" aria-hidden="true"><polygon points="23,2 44,14 44,36 23,48 2,36 2,14" fill="#0a7ee6"/><path d="M13 32h20M16 32l6-12 8 4" stroke="#fff" stroke-width="2.5" fill="none"/></svg>Dragline &amp; shovel maintenance</li>
    <li><svg width="46" height="50" viewBox="0 0 46 50" aria-hidden="true"><polygon points="23,2 44,14 44,36 23,48 2,36 2,14" fill="#0a7ee6"/><rect x="13" y="18" width="20" height="13" rx="2" stroke="#fff" stroke-width="2.5" fill="none"/><circle cx="23" cy="24.5" r="3" fill="#fff"/></svg>Great pay + long-term work</li>
    <li><svg width="46" height="50" viewBox="0 0 46 50" aria-hidden="true"><polygon points="23,2 44,14 44,36 23,48 2,36 2,14" fill="#0a7ee6"/><path d="M14 33V22h18v11zM12 22l4-6h14l4 6" stroke="#fff" stroke-width="2.5" fill="none"/></svg>Locally owned &amp; operated</li>
  </ul>

  <div class="brand"><span class="brand-mark"></span>KRT Site Services</div>

  <ul class="contact">
    <li><svg width="20" height="20" viewBox="0 0 20 20" aria-hidden="true"><circle cx="10" cy="10" r="10" fill="#0a7ee6"/><rect x="5" y="6.5" width="10" height="7" fill="none" stroke="#fff" stroke-width="1.5"/><path d="M5 7l5 4 5-4" stroke="#fff" stroke-width="1.5" fill="none"/></svg>jobs@krt.net.au</li>
    <li><svg width="20" height="20" viewBox="0 0 20 20" aria-hidden="true"><circle cx="10" cy="10" r="10" fill="#0a7ee6"/><path d="M7 5l2 3-1.5 1.5a7 7 0 0 0 3 3L12 11l3 2-1 2c-4 0-8-4-8-8z" fill="#fff"/></svg>+61 400 555 018</li>
  </ul>
</main>
</body>
</html>
```